依頼詳細
12月中旬にあらかじめ「親御さん」たちが目にとまるようチラシをまきたい。
記載項目
社名・募集項目・仕事の概要説明
サイズ
B4
ページ数
両面
希望イメージ
シンプル 複雑
単色 カラフル
暗い 明るい
日常 高級
遊び心 厳粛
未来的 伝統的
女性的 男性的
希望する色
水色系
納品ファイル
• イラストレーター形式 (.ai)
補足説明
参考資料です。
HPは http://www.kawabatakogyo.co.jp/
締め切り日が過ぎましたが、応募内容選定に時間が掛かっています。一週間の締め切り延期をさせていただきます。ご理解よろしくお願いします
■ 選んだ理由

力強さでした

■ 提案者全員のお礼・コメント

どの方も素晴らしく迷いました。これに懲りず今後もよろしくお願いします。

```html
<!DOCTYPE html>
<html lang="ja">
<head>
<meta charset="utf-8">
<title>地働地活 社員募集</title>
<link href="https://fonts.googleapis.com/css2?family=Noto+Sans+JP:wght@400;500;700&family=Kosugi+Maru&display=swap" rel="stylesheet">
<style>
  :root {
    --sky-deep: #1f6fc0;
    --sky-mid: #4d9be0;
    --sky-light: #a9d3f2;
    --sea: #2a7fc6;
    --paper: #ffffff;
    --ink: #1d3f6e;
    --text: #333a44;
    --line: #7fb4e0;
    --badge: #f29a2e;
  }
  * { margin: 0; padding: 0; box-sizing: border-box; }
  html, body { width: 878px; height: 1200px; overflow: hidden; background: var(--paper); }
  body { font-family: "Noto Sans JP", sans-serif; color: var(--text); position: relative; }

  .hero-photo {
    position: absolute; inset: 0 0 auto 0; height: 720px;
    background:
      linear-gradient(180deg, rgba(255,255,255,0) 70%, #fff 100%),
      linear-gradient(180deg, var(--sky-deep) 0%, var(--sky-mid) 30%, var(--sky-light) 52%, #6fb0e3 56%, var(--sea) 62%, #5ea6dc 80%, #dcecf8 100%);
  }
  .ruby {
    position: absolute; top: 180px; left: 0; width: 100%; text-align: center;
    font-family: "Kosugi Maru", sans-serif; font-size: 30px; letter-spacing: 58px; color: #fff;
    padding-left: 58px;
  }
  .title {
    position: absolute; top: 215px; left: 0; width: 100%; text-align: center;
    font-family: "Kosugi Maru", sans-serif; font-size: 104px; color: #fff; letter-spacing: 18px;
    text-shadow: 0 2px 8px rgba(20,60,120,.35);
  }
  .catch {
    position: absolute; top: 462px; left: 0; width: 100%; text-align: center;
    font-size: 24px; font-weight: 700; color: #fff; text-shadow: 0 1px 4px rgba(20,60,120,.5);
  }
  .intro {
    position: absolute; top: 515px; left: 0; width: 100%; text-align: center;
    font-size: 13px; line-height: 1.9; color: #fff;
  }
  .recruit {
    position: absolute; top: 660px; left: 218px; width: 442px;
    border: 1px solid var(--line); background: rgba(255,255,255,.92); padding: 12px 22px 14px;
  }
  .recruit-heading {
    text-align: center; font-size: 13px; font-weight: 700; color: var(--ink);
    border: 1px solid var(--line); width: 120px; margin: 0 auto 10px; padding: 2px 0;
  }
  .recruit-table { width: 100%; border-collapse: collapse; font-size: 10.5px; line-height: 1.65; }
  .recruit-table th { text-align: left; width: 76px; font-weight: 500; color: var(--ink); vertical-align: top; }
  .apply {
    position: absolute; top: 932px; left: 0; width: 100%; text-align: center; font-size: 11px;
  }
  .phone {
    position: absolute; top: 950px; left: 0; width: 100%; text-align: center;
    font-size: 19px; font-weight: 700; color: var(--ink); letter-spacing: 1px;
  }
  .phone svg { vertical-align: -3px; margin-right: 6px; }
  .note {
    position: absolute; top: 1005px; left: 0; width: 100%; text-align: center; font-size: 10.5px; color: var(--text);
  }
  .company {
    position: absolute; top: 1085px; left: 0; width: 100%; text-align: center;
  }
  .company-tag { font-size: 10px; color: var(--ink); display: block; margin-bottom: 2px; }
  .company-name { font-size: 30px; font-weight: 700; color: var(--ink); letter-spacing: 2px; }
  .company-name::before {
    content: ""; display: inline-block; width: 22px; height: 22px; border-radius: 50%;
    background: var(--sky-deep); margin-right: 10px; vertical-align: -2px;
  }
  .badge {
    position: absolute; top: 1040px; left: 752px; width: 96px; height: 96px; border-radius: 50%;
    background: var(--badge); color: #fff; font-size: 12px; font-weight: 700; text-align: center;
    display: flex; align-items: center; justify-content: center; line-height: 1.5;
  }
</style>
</head>
<body>
  <div class="hero-photo" role="img" aria-label="青空と白い雲、海に浮かぶ山のある島の風景写真"></div>

  <p class="ruby">ちどうちかつ</p>
  <h1 class="title">地働地活</h1>
  <p class="catch">大自然に恵まれたふるさとで、おもいっきり仕事ができる。</p>
  <p class="intro">
    豊かな自然と暮らしの中で、ふるさとの未来をつくる仕事をしませんか。<br>
    地域の道路や橋、港の整備を通じて、まちの安心と笑顔を支えています。<br>
    未経験の方も大歓迎。先輩社員が一から丁寧に指導いたします。
  </p>

  <section class="recruit">
    <h2 class="recruit-heading">社員募集要項</h2>
    <table class="recruit-table">
      <tr><th>■ 職　種</th><td>土木施工管理技術者／土木作業員／重機オペレーター</td></tr>
      <tr><th>■ 資　格</th><td>高卒以上、35歳位まで</td></tr>
      <tr><th>■ 勤務地</th><td>本社・現場（市内）</td></tr>
      <tr><th>■ 給　与</th><td>当社規定による（経験・能力を考慮します）</td></tr>
      <tr><th>■ 勤務時間</th><td>8:00〜17:00（休憩あり）</td></tr>
      <tr><th>■ 休　日</th><td>日曜・祝日・第2第4土曜、年末年始、夏季休暇</td></tr>
      <tr><th>■ 待　遇</th><td>社会保険完備、資格取得支援、退職金制度あり</td></tr>
      <tr><th>■ 応募方法</th><td>電話連絡の上、履歴書をご持参ください</td></tr>
    </table>
  </section>

  <p class="apply">詳細はお気軽にお問い合わせください。見学も随時受け付けています。</p>
  <p class="phone">
    <svg width="18" height="18" viewBox="0 0 24 24" aria-hidden="true"><path fill="#1d3f6e" d="M6.6 10.8a15 15 0 0 0 6.6 6.6l2.2-2.2a1 1 0 0 1 1-.25 11.4 11.4 0 0 0 3.6.57 1 1 0 0 1 1 1V20a1 1 0 0 1-1 1A17 17 0 0 1 3 4a1 1 0 0 1 1-1h3.5a1 1 0 0 1 1 1c0 1.25.2 2.45.57 3.57a1 1 0 0 1-.25 1z"/></svg>0120-5820-74
  </p>
  <p class="note">ホームページ http://www.kawabatakogyo.co.jp/ 受付時間 平日 8:00〜17:00</p>

  <div class="company">
    <span class="company-tag">ふるさとの未来をつくる</span>
    <span class="company-name">川端工業株式会社</span>
  </div>

  <div class="badge">Uターン就職<br>応援中!</div>
</body>
</html>
```